Complete Stationary Package Needed for New Dental Office ! ! !

I'm moving my dental office and would like to use my existing logo to create a new:
- Business Card (please submit Business Card designs to this project - http://work.pitchvault.net/brief.aspx?id=514296)
- Appointment Card (submit here)
- Letterhead (submit here)
- Envelope (submit here)
My practice name (within my logo) is:
Morris T. Lindqvist, D.D.S., P.A.
Family and Cosmetic Dentistry
***Obviously you will notice that the lower leg of the "K" in my logo is a smile.
My new address and contact information is:
372 Hollisbrook Lane, Suite 118
Fenwick Hollow, WK 27634
919-472-3081 (ph)
919-472-3095 (fax)
info@lindqvistdds.example
www.lindqvistdds.example
If you would like to use a tagline, I would suggest "Precision Dentistry with a Personal Touch".
I have attached my logo in numerous formats.
I have also attached 2 QR codes, one of which links to my website and the other one which links to a "Like" page for my business Chatterbook page. These QR codes could be improved by putting a graphic in the middle, but I created these myself and did not know how to do this.
Thank you for your time. I look forward to seeing all of your creative ideas!
Depending on the designs, I may award 2 different winners for the Business Card project and the Stationery Project. Or if a design is really good, I will award both projects to the same designer.
Updates
Project Deadline Extended
Reason: PitchVault administrators recently helped me split my project into 2 projects - 1 for business card and 1 for letterhead, envelope, etc. and I would like sufficient time to receive designs and provide feedback. Thank you.
Target Market(s)
Current and prospective dental patients.
Industry/Entity Type
Dental
Requirements
Must have
- Please ensure business card has a 2-sided design.
- Please ensure that your design is "practical" for printing purposes.
Nice to have
- Improvement of QR codes by addition of graphics in the middle to differentiate them. Incorporation of QR codes into business card design, maybe on the back side? I would consider the Chatterbook QR code more important than the website QR code simply because my website URL is very easy to type.
Should not have
- Please, NO "floating" or "extracted" teeth which sends an undesirable message.

```html
<!DOCTYPE html>
<html lang="en">
<head>
<meta charset="utf-8">
<title>Morris T. Lindqvist, D.D.S., P.A. — Envelope</title>
<link rel="stylesheet" href="https://fonts.googleapis.com/css2?family=Cormorant+Garamond:wght@500;600&display=swap">
<style>
  :root {
    --backdrop: #c9c9c9;
    --paper: #f1f1f1;
    --navy-deep: #0e1a4f;
    --navy: #1f3a97;
    --ink: #1d2340;
    --teal: #2f7a6e;
    --flap-text: #8fa0d8;
  }
  html, body {
    margin: 0;
    width: 1200px;
    height: 777px;
    overflow: hidden;
    background: var(--backdrop);
  }
  .stationery {
    position: relative;
    width: 1200px;
    height: 777px;
  }
  .envelope {
    position: absolute;
    left: 190px;
    width: 820px;
    height: 356px;
    background: var(--paper);
    box-shadow: 0 2px 6px rgba(0,0,0,0.12);
    overflow: hidden;
    font-family: "Cormorant Garamond", Georgia, serif;
    color: var(--ink);
  }
  .envelope--front { top: 22px; }
  .envelope--back { top: 400px; }

  .front-band {
    position: absolute;
    left: 0; top: 0;
    width: 820px; height: 22px;
  }
  .brand {
    position: absolute;
    left: 34px;
    top: 42px;
  }
  .brand-name {
    display: flex;
    align-items: center;
    gap: 8px;
    font-size: 19px;
    font-weight: 600;
    letter-spacing: 0.06em;
    text-transform: uppercase;
    color: var(--ink);
  }
  .brand-mark {
    width: 20px; height: 20px;
    background: var(--navy);
  }
  .brand-tagline {
    margin: 2px 0 0 28px;
    font-size: 10px;
    font-weight: 500;
    letter-spacing: 0.12em;
    text-transform: uppercase;
    color: var(--teal);
  }
  .contact-list {
    position: absolute;
    left: 34px;
    bottom: 30px;
    margin: 0; padding: 0;
    list-style: none;
    font-size: 12px;
    font-weight: 500;
    letter-spacing: 0.05em;
    text-transform: uppercase;
  }
  .contact-item {
    display: flex;
    align-items: flex-start;
    gap: 10px;
    margin-top: 9px;
    line-height: 1.3;
  }
  .contact-icon {
    flex: none;
    width: 16px; height: 16px;
  }

  .back-flap {
    position: absolute;
    left: 0; top: 0;
    width: 820px; height: 120px;
  }
  .flap-url {
    position: absolute;
    left: 0; right: 0;
    top: 44px;
    text-align: center;
    font-size: 15px;
    font-weight: 500;
    letter-spacing: 0.32em;
    text-transform: uppercase;
    color: var(--flap-text);
  }
</style>
</head>
<body>
<main class="stationery">

  <section class="envelope envelope--front" aria-label="Envelope front">
    <svg class="front-band" viewBox="0 0 820 22" preserveAspectRatio="none" aria-hidden="true">
      <defs>
        <linearGradient id="bandGrad" x1="0" y1="0" x2="1" y2="0">
          <stop offset="0" stop-color="#1f3a97"/>
          <stop offset="1" stop-color="#0e1a4f"/>
        </linearGradient>
      </defs>
      <rect x="0" y="0" width="820" height="22" fill="url(#bandGrad)"/>
    </svg>

    <div class="brand">
      <div class="brand-name"><span class="brand-mark"></span>Morris T. Lindqvist, D.D.S., P.A.</div>
      <div class="brand-tagline">Family and Cosmetic Dentistry</div>
    </div>

    <ul class="contact-list">
      <li class="contact-item">
        <svg class="contact-icon" viewBox="0 0 16 16" aria-hidden="true"><path d="M4 1.5l2.4 3-1.5 1.6c.8 1.9 2.2 3.3 4.1 4.1l1.6-1.5 3 2.4-1.3 2.6C7 13.5 2.5 9 1.7 2.8z" fill="#1d2340"/></svg>
        <span>919-472-3081</span>
      </li>
      <li class="contact-item">
        <svg class="contact-icon" viewBox="0 0 16 16" aria-hidden="true"><rect x="4" y="1.5" width="8" height="4" fill="none" stroke="#1d2340" stroke-width="1.4"/><rect x="1.5" y="5.5" width="13" height="6" rx="1" fill="#1d2340"/><rect x="4" y="10" width="8" height="4.5" fill="#f1f1f1" stroke="#1d2340" stroke-width="1.4"/></svg>
        <span>919-472-3095</span>
      </li>
      <li class="contact-item">
        <svg class="contact-icon" viewBox="0 0 16 16" aria-hidden="true"><circle cx="8" cy="8" r="6.5" fill="none" stroke="#1d2340" stroke-width="1.4"/><ellipse cx="8" cy="8" rx="2.8" ry="6.5" fill="none" stroke="#1d2340" stroke-width="1.2"/><path d="M1.5 8h13M2.6 4.6h10.8M2.6 11.4h10.8" stroke="#1d2340" stroke-width="1.1"/></svg>
        <span>www.lindqvistdds.example</span>
      </li>
      <li class="contact-item">
        <svg class="contact-icon" viewBox="0 0 16 16" aria-hidden="true"><path d="M8 15.5s-5-5.2-5-9a5 5 0 0 1 10 0c0 3.8-5 9-5 9z" fill="#1d2340"/><circle cx="8" cy="6.5" r="1.9" fill="#f1f1f1"/></svg>
        <span>372 Hollisbrook Lane, Suite 118<br>Fenwick Hollow, WK 27634</span>
      </li>
    </ul>
  </section>

  <section class="envelope envelope--back" aria-label="Envelope back">
    <svg class="back-flap" viewBox="0 0 820 120" preserveAspectRatio="none" aria-hidden="true">
      <defs>
        <linearGradient id="flapGrad" x1="0" y1="0" x2="1" y2="1">
          <stop offset="0" stop-color="#0e1a4f"/>
          <stop offset="0.6" stop-color="#182d7c"/>
          <stop offset="1" stop-color="#2443a6"/>
        </linearGradient>
      </defs>
      <path d="M0 0H820V82Q820 120 782 120H0Z" fill="url(#flapGrad)"/>
    </svg>
    <div class="flap-url">www.lindqvistdds.example</div>
  </section>

</main>
</body>
</html>
```